Website Design for a Project Management Consulting Business

I have a logo design already and now I need a website.
I am a project manager and run my own consulting business.
Currently I am under contract with 3 major Kestrelmark 300 companies. I'd like a website I can direct current and future clients.
My job is running IT projects and working with developers to deliver business priorities.
The website should be professional and clean - I work IT projects and would like to incorporate that into any theme.
I'd like the site to have several page or breakoff links - sections would include : about me, about my services, a page to display all of my certification badges, another page to talk about highlights from past projects and so on.
Looking for a collaborative experience.

Industry/Entity Type

Kestrelmark 300 Consulting Firm - Project Management

Coding

Coded - Design and coding required

Number of Pages Required

1 page

Font styles to use
Serif

Colors
0094D4
00A9DD
6FCCEA
C7EBF8
E9F6FB
EE7325
F08F49
F5BC92
FAE3D3
FDF4ED

Requirements
Must have
• Sections that are a must: About Me (bio), About My Services, About my Certifications and Credentials, Experience on Past Projects,
Nice to have
• I have added the logo below - I'd like to use the logo and have it prominent ; should be professional and inviting

```html
<!DOCTYPE html>
<html lang="en">
<head>
<meta charset="utf-8">
<title>Project Management Northline LLC</title>
<link rel="stylesheet" href="https://fonts.googleapis.com/css2?family=Playfair+Display:wght@400;700&family=Poppins:wght@400;500;600;800&display=swap">
<style>
:root{
  --blue:#0094D4;
  --blue-bright:#00A9DD;
  --blue-soft:#6FCCEA;
  --blue-pale:#C7EBF8;
  --blue-mist:#E9F6FB;
  --orange:#EE7325;
  --orange-soft:#F08F49;
  --orange-pale:#F5BC92;
  --navy:#0f2a60;
  --navy-deep:#0b1f58;
  --ink:#5b6270;
  --white:#ffffff;
  --serif:'Playfair Display', Georgia, serif;
  --sans:'Poppins', Arial, sans-serif;
}
*{box-sizing:border-box;margin:0;padding:0}
html,body{width:1200px;height:3873px;overflow:hidden}
body{position:relative;background:var(--white);font-family:var(--sans);color:var(--ink)}
.abs{position:absolute}
a{color:inherit}

/* header */
.site-header{position:absolute;left:0;top:0;width:1200px;height:72px;background:#fff}
.brand{position:absolute;display:flex;align-items:center;gap:8px;color:var(--navy);font-family:var(--sans);font-weight:500}
.brand .mark{width:30px;height:30px;border:3px solid var(--navy)}
.brand .name{font-size:24px;line-height:1;letter-spacing:.5px}
.site-header .brand{left:58px;top:20px}
.main-nav{position:absolute;left:370px;top:28px;display:flex;gap:34px;font-size:14px;color:var(--navy)}
.main-nav .active{color:var(--blue)}
.btn{display:flex;align-items:center;justify-content:space-between;border-radius:20px;font-family:var(--sans);font-weight:600;font-size:13px;letter-spacing:.5px;padding:0 6px 0 20px;white-space:nowrap}
.btn .ico{width:24px;height:24px;border-radius:50%;background:var(--orange);display:flex;align-items:center;justify-content:center}
.btn-blue{background:var(--blue);color:#fff}
.btn-outline{border:2px solid var(--blue);color:var(--blue);background:#fff}
.get-in-touch{left:980px;top:21px;width:160px;height:35px}

/* hero */
.hero-photo{left:0;top:72px;width:1200px;height:507px;background:linear-gradient(90deg,#2b4a7b 0%,#3f6495 40%,#6f8fb8 70%,#8aa3c3 100%)}
.hero-title{left:160px;top:208px;font-family:var(--serif);font-weight:700;font-size:52px;line-height:56px;color:#fff;letter-spacing:1px}
.hero .btn{left:158px;top:403px;width:143px;height:33px}

/* credentials */
.badges{left:0;top:579px;width:1200px;height:150px;border-bottom:1px solid #e3e6ea}
.badge{position:absolute;top:24px;width:105px;height:105px;border-radius:50%;background:var(--blue-mist);border:2px solid var(--blue-pale)}
.badge-tab{position:absolute;left:591px;top:147px;width:159px;height:3px;background:var(--blue)}

/* about */
.about-panel{left:159px;top:854px;width:379px;height:379px;background:linear-gradient(160deg,#1c6aa0,#0d4f86)}
.about-portrait{left:200px;top:782px;width:300px;height:451px;background:linear-gradient(180deg,#7d8fb6 0%,#6178a7 60%,#4b5f8e 100%);border-radius:120px 120px 0 0}
.eyebrow{font-size:14px;letter-spacing:.5px;color:var(--blue)}
.eyebrow.caps{text-transform:uppercase;letter-spacing:1px}
.about-eyebrow{left:601px;top:834px}
.heading{font-family:var(--serif);font-weight:400;font-size:37px;line-height:39px;color:var(--navy);letter-spacing:1px}
.about-heading{left:599px;top:858px}
.copy{font-size:13px;line-height:21px;color:var(--ink)}
.about-copy{left:602px;top:950px;width:410px}
.about-copy p+p{margin-top:21px}
.about-btn{left:604px;top:1168px;width:232px;height:37px}

/* projects */
.projects{left:0;top:1354px;width:1200px;height:619px;background:var(--blue);overflow:hidden}
.projects-word{position:absolute;left:150px;top:-10px;writing-mode:vertical-rl;transform:rotate(180deg);font-family:var(--sans);font-weight:800;font-size:112px;letter-spacing:6px;color:rgba(255,255,255,.4);height:640px;line-height:1}
.project-card{position:absolute;top:1328px;width:320px;text-align:center;color:#fff}
.project-card .shot{height:409px;border:2px solid rgba(255,255,255,.7)}
.project-card h3{margin-top:24px;font-family:var(--serif);font-weight:400;font-size:22px;letter-spacing:1px;white-space:nowrap}
.project-card p{margin:10px auto 0;width:270px;font-size:13px;line-height:19px;color:#e6f4fb}
.project-card a{display:inline-block;margin-top:18px;font-size:13px;text-decoration:underline;text-underline-offset:4px}

/* services */
.services-eyebrow{left:160px;top:2066px}
.services-heading{left:158px;top:2090px}
.all-services{left:889px;top:2090px;width:153px;height:35px}
.service-card{position:absolute;top:2173px;width:200px;height:263px;background:#fff;box-shadow:0 6px 26px rgba(15,42,96,.08)}
.service-card .num{position:absolute;left:26px;top:3px;width:63px;height:68px;background:#fff;border:2px solid var(--blue-pale);border-top:0;display:flex;align-items:center;justify-content:center}
.service-card .num span{display:flex;align-items:center;justify-content:center;width:55px;height:58px;background:var(--blue);color:#fff;font-family:var(--serif);font-size:36px}
.service-card.is-orange .num span{background:var(--orange)}
.service-card h3{position:absolute;left:26px;top:92px;font-family:var(--serif);font-weight:400;font-size:18px;line-height:21px;color:#333a47;letter-spacing:.5px;white-space:nowrap}
.service-card p{position:absolute;left:26px;top:144px;width:160px;font-size:12.5px;line-height:21px}
.service-card a{position:absolute;left:26px;top:216px;font-size:12.5px;color:var(--blue);text-decoration:underline;text-underline-offset:3px}
.service-card.is-orange a{color:var(--orange)}

/* stats */
.stats-photo{left:0;top:2533px;width:1200px;height:276px;background:linear-gradient(100deg,#0d2d7a 0%,#16409a 50%,#0e2f80 100%)}
.stat{position:absolute;top:2612px;width:260px;text-align:center;color:#fff}
.stat .label{font-size:13px;letter-spacing:1.5px}
.stat .value{font-weight:800;font-size:40px;line-height:44px;letter-spacing:1px}
.stat .sub{font-family:var(--serif);font-weight:700;font-size:19px;letter-spacing:1px}
.stat a{display:inline-block;margin-top:14px;font-size:14px;text-decoration:underline;text-underline-offset:4px}

/* contact */
.contact-eyebrow{left:160px;top:2896px}
.contact-heading{left:158px;top:2922px}
.contact-copy{left:158px;top:3060px;width:420px}
.call-dot{left:158px;top:3143px;width:53px;height:53px;border-radius:50%;background:var(--orange)}
.call-label{left:225px;top:3156px;font-size:12px;color:var(--orange)}
.call-number{left:225px;top:3172px;font-size:16px;font-weight:600;color:var(--navy)}
.callback-btn{left:158px;top:3226px;width:223px;height:34px}
.field{position:absolute;border:1.5px solid var(--orange-pale);border-radius:19px;font-size:12.5px;color:#8a8f98;padding:0 20px;display:flex;align-items:center}
.field.area{align-items:flex-start;padding-top:14px;border-radius:24px}
.send{left:627px;top:3179px;width:415px;height:56px;background:var(--orange);color:#fff;font-weight:600;font-size:15px;letter-spacing:1px;display:flex;align-items:center;justify-content:center;gap:8px}

/* clients */
.clients{left:0;top:3355px;width:1200px;height:137px;background:var(--blue-mist)}
.client{position:absolute;top:3410px;width:160px;font-family:var(--sans);font-weight:600;font-size:16px;color:#4a5466;display:flex;align-items:center;justify-content:center;gap:8px;white-space:nowrap}
.client i{display:inline-block;width:14px;height:14px;background:#4a5466}

/* footer */
.site-footer{left:0;top:3492px;width:1200px;height:381px;background:var(--navy-deep);color:#fff}
.footer-brand{left:158px;top:3625px;color:#fff}
.footer-brand .mark{border-color:#fff}
.social{left:160px;top:3676px;display:flex;gap:11px}
.social span{width:18px;height:18px;border:1.5px solid #fff;border-radius:50%}
.foot-col{position:absolute;top:3576px;font-size:12.5px;color:#fff}
.foot-col h4{font-weight:600;font-size:14px;letter-spacing:1px;margin-bottom:22px}
.foot-col li{list-style:none;height:26px}
.foot-col .phone{color:var(--orange);font-weight:600;font-size:16px;margin-bottom:12px}
.copyright{left:0;top:3843px;width:1200px;text-align:center;font-size:11px;color:#d8def0}
</style>
</head>
<body>

<header class="site-header">
  <div class="brand"><span class="mark"></span><span class="name">NORTHLINE</span></div>
  <nav class="main-nav">
    <span class="active">Home</span><span>About Us</span><span>Services ▾</span><span>Success ▾</span><span>Careers</span><span>Contact Us</span>
  </nav>
  <div class="abs btn btn-blue get-in-touch">GET IN TOUCH <span class="ico"><svg width="12" height="12" viewBox="0 0 12 12"><path d="M2 10L10 2M4 2h6v6" stroke="#fff" stroke-width="1.8" fill="none"/></svg></span></div>
</header>

<section class="hero">
  <div class="abs hero-photo" role="img" aria-label="Two smiling business colleagues in an office reviewing a laptop together"></div>
  <h1 class="abs hero-title">The Fastest<br>Way to Achieve<br>Success</h1>
  <div class="abs btn btn-blue">LEARN MORE <span class="ico"><svg width="12" height="12" viewBox="0 0 12 12"><path d="M2 10L10 2M4 2h6v6" stroke="#fff" stroke-width="1.8" fill="none"/></svg></span></div>
</section>

<section class="abs badges" aria-label="Certifications">
  <span class="badge" style="left:186px"></span>
  <span class="badge" style="left:398px"></span>
  <span class="badge" style="left:616px"></span>
  <span class="badge" style="left:847px"></span>
  <span class="badge-tab"></span>
</section>

<section class="about">
  <div class="abs about-panel"></div>
  <div class="abs about-portrait" role="img" aria-label="Portrait of the consultant in a plaid blazer and tie"></div>
  <p class="abs eyebrow about-eyebrow">About Comapny</p>
  <h2 class="abs heading about-heading">Creating A Business<br>With Authentic Integrity</h2>
  <div class="abs copy about-copy">
    <p>Lorem ipsum dolor sit amet, consectetur adipiscing elit, sed do eiusmod tempor incididunt ut labore et dolore magna aliqua. Ut enim ad minim veniam, quis nostrud exercitation ullamco laboris nisi ut aliquip ex ea commodo consequat. Duis aute irure dolor in repreh.</p>
    <p>Enderit in voluptate velit esse cillum dolore eu fugiat nulla pariatur. Excepteur sint occaecat cupidatat non proident, sunt in culpa qui officia deserunt mo...</p>
  </div>
  <div class="abs btn btn-outline about-btn">More About Company <span class="ico"><svg width="12" height="12" viewBox="0 0 12 12"><path d="M2 10L10 2M4 2h6v6" stroke="#fff" stroke-width="1.8" fill="none"/></svg></span></div>
</section>

<section class="abs projects"><span class="projects-word">PROJECTS</span></section>
<article class="project-card" style="left:340px">
  <div class="shot" role="img" aria-label="Laptop on a desk showing lines of code" style="background:linear-gradient(160deg,#e9eaec,#9a9ea6 55%,#2b2e35)"></div>
  <h3>ED UT PERSPICIA</h3>
  <p>Lorem ipsum dolor sit amet, consectetur adipiscing elit, sed doe iusmod tempor incidid</p>
  <a>LEARN MORE</a>
</article>
<article class="project-card" style="left:662px">
  <div class="shot" role="img" aria-label="Developer working at a laptop in a busy workspace" style="background:linear-gradient(180deg,#6b5f52 0%,#a7764e 45%,#ee7325 100%)"></div>
  <h3>QUIS AUTEM VEL EU</h3>
  <p>Lorem ipsum dolor sit amet, consectetur adipiscing elit, sed doe iusmod tempor incidid</p>
  <a>LEARN MORE</a>
</article>
<article class="project-card" style="left:984px">
  <div class="shot" role="img" aria-label="Business growth book beside a coffee mug" style="background:linear-gradient(160deg,#d9d4cc,#8c8178 55%,#2a2522)"></div>
  <h3>NUMQUAM EIUS</h3>
  <p>Lorem ipsum dolor sit amet, consectetur adipiscing elit, sed doe iusmod tempor incidid</p>
  <a>LEARN MORE</a>
</article>

<section class="services">
  <p class="abs eyebrow caps services-eyebrow">What we do</p>
  <h2 class="abs heading services-heading">Consulting Services</h2>
  <div class="abs btn btn-blue all-services">ALL SERVICES <span class="ico"><svg width="12" height="12" viewBox="0 0 12 12"><path d="M2 10L10 2M4 2h6v6" stroke="#fff" stroke-width="1.8" fill="none"/></svg></span></div>
  <article class="service-card" style="left:158px"><div class="num"><span>01</span></div><h3>Finance and<br>Restructuring</h3><p>Neque porro quisquam est, qui dolorem ipsum quia dolor sit</p><a>LEARN MORE</a></article>
  <article class="service-card" style="left:387px"><div class="num"><span>02</span></div><h3>Audit<br>and Assurance</h3><p>Neque porro quisquam est, qui dolorem ipsum quia dolor sit</p><a>LEARN MORE</a></article>
  <article class="service-card is-orange" style="left:614px"><div class="num"><span>03</span></div><h3>Strategy<br>and Planning</h3><p>Neque porro quisquam est, qui dolorem ipsum quia dolor sit</p><a>LEARN MORE</a></article>
  <article class="service-card" style="left:842px"><div class="num"><span>04</span></div><h3>Trades<br>and Stock Market</h3><p>Neque porro quisquam est, qui dolorem ipsum quia dolor sit</p><a>LEARN MORE</a></article>
</section>

<section class="stats">
  <div class="abs stats-photo" role="img" aria-label="Desk with papers, glasses and photographs under a deep blue tint"></div>
  <div class="stat" style="left:172px"><p class="label">PROJECTS</p><p class="value">2.5K</p><p class="sub">Successful Projects</p><a>Our Projects</a></div>
  <div class="stat" style="left:470px"><p class="label">OUR TEAM</p><p class="value">138+</p><p class="sub">Experienced Staff</p><a>Team Members</a></div>
  <div class="stat" style="left:766px"><p class="label">HAPPY CLIENTS</p><p class="value">99%</p><p class="sub">Client Satisfaction</p><a>Testimonials</a></div>
</section>

<section class="contact">
  <p class="abs eyebrow caps contact-eyebrow">Contact us</p>
  <h2 class="abs heading contact-heading">Start A New<br>Case? Contact Our<br>Experts</h2>
  <p class="abs copy contact-copy">Quis autem vel eum iure reprehenderit qui in ea voluptate velit esse quam nihil molestiae consequatur, vel illum qui do lorem eum fugiat quo voluptas?</p>
  <div class="abs call-dot"></div>
  <p class="abs call-label">HAVE A QUESTION?</p>
  <p class="abs call-number">+888 410 22 319</p>
  <div class="abs btn btn-blue callback-btn">REQUEST A CALL BACK <span class="ico"><svg width="12" height="12" viewBox="0 0 12 12"><path d="M2 10L10 2M4 2h6v6" stroke="#fff" stroke-width="1.8" fill="none"/></svg></span></div>
  <div class="field" style="left:624px;top:2940px;width:206px;height:37px">Name*</div>
  <div class="field" style="left:836px;top:2940px;width:206px;height:37px">Email*</div>
  <div class="field" style="left:624px;top:2984px;width:206px;height:37px">Phone*</div>
  <div class="field" style="left:836px;top:2984px;width:206px;height:37px">Discuss About</div>
  <div class="field area" style="left:624px;top:3031px;width:418px;height:136px">Message*</div>
  <div class="abs send"><svg width="20" height="18" viewBox="0 0 20 18"><path d="M1 8L19 1 15 17 10 12 7 16 7 11 16 4 6 10Z" fill="#fff"/></svg>SEND MESSAGE</div>
</section>

<section class="abs clients" aria-label="Clients"></section>
<div class="client" style="left:135px"><i></i>Vantor Power</div>
<div class="client" style="left:290px">Clearview Optics</div>
<div class="client" style="left:445px">Harbor Bank Group</div>
<div class="client" style="left:605px">Ridgeway Motors</div>
<div class="client" style="left:758px">Calloway</div>
<div class="client" style="left:915px"><i style="width:16px;height:16px;background:#6a1fb5"></i>Telvia</div>

<footer class="abs site-footer"></footer>
<div class="brand footer-brand"><span class="mark"></span><span class="name">NORTHLINE</span></div>
<div class="abs social"><span></span><span></span><span></span><span></span></div>
<div class="foot-col" style="left:417px"><h4>SERVICES</h4><ul><li>Rem ipsum dolor</li><li>Sit ametconse</li><li>Cetur adipiscing</li><li>Elit seddoeiu</li><li>Smod Perspiciatis</li></ul></div>
<div class="foot-col" style="left:644px"><h4>ABOUT</h4><ul><li>Rem ipsum dolor</li><li>Sit ametconse</li><li>Cetur adipiscing</li><li>Elit seddoeiu</li><li>Smod Perspiciatis</li></ul></div>
<div class="foot-col" style="left:836px;width:190px"><h4>CONTACT US</h4><p class="phone">(+012) 555 -019</p><p style="margin-bottom:16px">info@northlinellc.com</p><p style="line-height:16px">123, Lorem ipsum dolor sit amet, consectetur Adipiscing</p></div>
<p class="abs copyright">© Copyright 2022 Northline Consulting. All rights reserved.</p>

</body>
</html>
```